Can you make our site AWESOME?

Hi Guys,

I am a co-founder of Tumble Crate Rentals Oz, the world's first e-commerce skip bin business.

We are looking to update our site before a launch into the UK in March.

Please help us by submitting your designs for the following pages:

- Home page (www.tumblecraterentalsoz.example.au)
- About us (https://www.tumblecraterentalsoz.example.au/pages/about-us
- Contact us (https://www.tumblecraterentalsoz.example.au/pages/contact-us)
- Quick Quote / Pricing (https://www.tumblecraterentalsoz.example.au/pages/free-instant-quote-skip-bin-hire)

NOTES:
- Design should be high-converting
- best designs will be fresh, modern, easy to read, distinctive and memorable
- please use our logo and video colours
- feel free to change logos, layout, images and anything else you feel can be improved
- the winning designer will potentially have the opportunity to re-design the other pages on our site
- brief is for design only

Any questions just ask.

Thanks,
Morton

```html
<!DOCTYPE html>
<html lang="en">
<head>
<meta charset="utf-8">
<title>Tumble Crate Rentals Oz – Home</title>
<link rel="stylesheet" href="https://fonts.googleapis.com/css2?family=Quicksand:wght@500;600;700&family=Open+Sans:wght@400;600;700&display=swap">
<style>
:root{
  --navy:#24235c;
  --navy-deep:#1c1b4a;
  --green:#3aaa35;
  --green-dark:#1f6b2a;
  --green-mid:#2e8f33;
  --ink:#2b2b4f;
  --text:#555;
  --grey-band:#ebebeb;
  --star:#f5c518;
  --white:#fff;
}
*{box-sizing:border-box;margin:0;padding:0}
html,body{width:1200px;height:3303px;overflow:hidden;background:var(--white)}
body{position:relative;font-family:"Open Sans",Arial,sans-serif;color:var(--text)}
.abs{position:absolute}

/* header */
.site-header{left:0;top:0;width:1200px;height:92px;background:var(--white)}
.brand{left:145px;top:26px;display:flex;align-items:center;gap:14px}
.brand-mark{width:40px;height:40px;background:var(--navy);border-radius:6px}
.brand-name{font-family:"Quicksand",sans-serif;font-weight:700;font-size:25px;color:var(--navy);letter-spacing:.5px}
.phone{left:862px;top:33px;font-size:19px;color:var(--ink);display:flex;align-items:center;gap:6px}
.cart{left:1014px;top:25px;width:42px;height:42px;border-radius:50%;background:var(--green);display:flex;align-items:center;justify-content:center}
.main-nav{left:0;top:92px;width:1200px;height:40px;background:var(--navy)}
.main-nav a{position:absolute;top:12px;transform:translateX(-50%);font-size:12.5px;color:#b9b9d6;text-decoration:none;text-transform:uppercase;letter-spacing:.3px;white-space:nowrap}
.main-nav a.active{color:var(--white);font-weight:600}

/* hero */
.hero{left:0;top:132px;width:1200px;height:482px;background:linear-gradient(180deg,#3a3f6b,#2a2d55 60%,#343a66)}
.hero-title{left:0;width:1200px;text-align:center;font-family:"Quicksand",sans-serif;font-weight:700;color:var(--white)}
.hero-sub{left:0;width:1200px;text-align:center;font-size:19px;color:var(--white);letter-spacing:.3px}
.quote-box{left:361px;width:478px;height:50px;border-radius:25px;background:var(--white);display:flex;align-items:center;justify-content:space-between;padding:0 5px 0 30px}
.quote-box span{font-size:15px;color:#555}
.quote-btn{height:38px;padding:0 20px;border-radius:19px;background:var(--green);color:var(--white);font-weight:700;font-size:15px;display:flex;align-items:center}
.stars{left:0;width:1200px;display:flex;justify-content:center;gap:4px}
.hero-arrow{top:358px}

/* categories */
.cat{width:164px;height:164px;border:3px solid var(--green);border-radius:50%;display:flex;flex-direction:column;align-items:center;justify-content:center;gap:10px;top:693px}
.cat span{font-family:"Quicksand",sans-serif;font-weight:600;font-size:20px;color:var(--green)}
.tagline{left:0;top:884px;width:1200px;text-align:center;font-family:"Quicksand",sans-serif;font-weight:600;font-size:23px;color:#555}

/* steps */
.steps{left:0;top:993px;width:600px;height:647px;background:var(--green)}
.steps-title{left:145px;top:1065px;font-family:"Quicksand",sans-serif;font-weight:600;font-size:38px;color:var(--white)}
.step-line{left:206px;top:1206px;width:2px;height:296px;background:var(--white)}
.step-ring{left:145px;width:124px;height:124px;border:2px solid var(--white);border-radius:50%;background:var(--green);display:flex;align-items:center;justify-content:center}
.step-text{left:286px;width:260px;color:var(--white)}
.step-text h3{font-family:"Quicksand",sans-serif;font-weight:700;font-size:18px;margin-bottom:6px}
.step-text p{font-size:12px;line-height:1.5}
.video-panel{left:600px;top:993px;width:600px;height:647px;background:var(--green-dark)}
.map-area{left:700px;top:1110px;width:420px;height:420px;border-radius:40% 50% 45% 55%;background:radial-gradient(circle at 50% 50%,#2a8a34,#23752e 70%,rgba(31,107,42,0))}
.video-text{left:640px;top:1298px;width:520px;text-align:center;font-family:"Quicksand",sans-serif;font-weight:600;font-size:24px;line-height:1.5;color:var(--white)}

/* testimonials */
.section-title{left:0;width:1200px;text-align:center;font-family:"Quicksand",sans-serif;font-weight:600;color:var(--ink)}
.review{text-align:center}
.review p{font-size:13px;line-height:1.65;color:#555}
.review .who{font-size:12px;font-weight:700;color:#333;margin-top:12px}
.review .date{font-size:12px;color:#333}
.avatar{border-radius:50%;background:linear-gradient(160deg,#c9c3be,#8d8b91)}
.review-card{left:434px;top:1783px;width:332px;height:400px;background:var(--white);box-shadow:0 0 28px rgba(0,0,0,.12)}
.mini-stars{display:flex;justify-content:center;gap:3px;margin-top:6px}
.mini-stars i{width:16px;height:16px;background:var(--green)}
.review-card-stars i{width:24px;height:24px}

/* benefits */
.benefits{left:0;top:2213px;width:1200px;height:418px;background:var(--grey-band)}
.benefit{width:230px;text-align:center;top:2360px}
.benefit h4{font-family:"Quicksand",sans-serif;font-weight:600;font-size:16px;color:var(--green);margin:14px 0 10px;line-height:1.3}
.benefit p{font-size:10.5px;line-height:1.6;color:#555}

/* cta */
.cta-title{left:0;top:2700px;width:1200px;text-align:center;font-family:"Quicksand",sans-serif;font-weight:700;font-size:41px;color:var(--green)}
.cta-sub{color:var(--ink)}
.cta .quote-box{background:#ececec}

/* footer */
.site-footer{left:0;top:2981px;width:1200px;height:322px;background:var(--navy)}
.fcol h5{font-family:"Quicksand",sans-serif;font-weight:500;font-size:18px;color:var(--white);margin-bottom:14px;white-space:nowrap}
.fcol h5.fcol-wide{font-size:15px;line-height:22px}
.fcol li{list-style:none;font-size:11px;color:#c4c4de;line-height:22.5px}
.news-input{left:839px;top:3060px;width:218px;height:40px;background:#cfd0e6;display:flex;align-items:center;justify-content:space-between;padding:0 12px 0 16px;font-size:12px;color:#555}
.copyright{left:145px;top:3246px;font-size:11px;color:#c4c4de}
.pay{top:3244px;height:22px;border:1px solid #8e8fb8;border-radius:3px;background:rgba(255,255,255,.08)}
.social{top:3246px;width:16px;height:16px;border-radius:50%;background:#b7b8d6}
</style>
</head>
<body>

<header class="abs site-header">
  <div class="abs brand"><div class="brand-mark"></div><div class="brand-name">Tumble Crate Rentals Oz</div></div>
  <div class="abs phone">
    <svg width="16" height="16" viewBox="0 0 24 24"><path fill="#2b2b4f" d="M6.6 10.8a15.1 15.1 0 0 0 6.6 6.6l2.2-2.2c.3-.3.7-.4 1-.2 1.1.4 2.3.6 3.6.6.6 0 1 .4 1 1V20c0 .6-.4 1-1 1A17 17 0 0 1 3 4c0-.6.4-1 1-1h3.5c.6 0 1 .4 1 1 0 1.3.2 2.5.6 3.6.1.3 0 .7-.2 1z"/></svg>
    1800 555 019
  </div>
  <div class="abs cart"><svg width="18" height="18" viewBox="0 0 24 24"><path d="M3 4h3l2.5 10h10l2-7H8" stroke="#fff" stroke-width="2" fill="none"/><circle cx="10" cy="19" r="2" fill="#fff"/><circle cx="17" cy="19" r="2" fill="#fff"/></svg></div>
</header>

<nav class="abs main-nav">
  <a class="active" style="left:170px">Pricing</a>
  <a style="left:306px">Learn More</a>
  <a style="left:438px">About</a>
  <a style="left:583px">Trade Secrets</a>
  <a style="left:733px">Contact</a>
  <a style="left:852px">Login</a>
  <a style="left:1000px">Create Account</a>
</nav>

<section class="abs hero" role="img" aria-label="Aerial photo of a suburban neighbourhood under a navy overlay"></section>
<h1 class="abs hero-title" style="top:266px;font-size:42px">1000's of Skips at Your Finger Tips</h1>
<p class="abs hero-sub" style="top:333px">BEST SERVICE &amp; PRICE &nbsp;•&nbsp; HASSLE FREE &nbsp;•&nbsp; AUSTRALIA WIDE</p>
<div class="abs quote-box" style="top:374px"><span>Enter Postcode or Suburb</span><div class="quote-btn">INSTANT QUOTE</div></div>
<div class="abs stars" style="top:442px">
  <svg width="130" height="26" viewBox="0 0 130 26"><g fill="#f5c518"><path id="s" d="M13 1l3.5 7.6 8.3.9-6.2 5.6 1.8 8.2L13 19l-7.4 4.3 1.8-8.2L1.2 9.5l8.3-.9z"/><use href="#s" x="26"/><use href="#s" x="52"/><use href="#s" x="78"/><use href="#s" x="104"/></g></svg>
</div>
<svg class="abs hero-arrow" style="left:52px" width="14" height="24" viewBox="0 0 14 24"><path d="M12 2 3 12l9 10" stroke="#fff" stroke-width="3" fill="none"/></svg>
<svg class="abs hero-arrow" style="left:1130px" width="14" height="24" viewBox="0 0 14 24"><path d="M2 2l9 10-9 10" stroke="#fff" stroke-width="3" fill="none"/></svg>

<!-- categories -->
<div class="abs cat" style="left:145px">
  <svg width="60" height="54" viewBox="0 0 60 54" fill="none" stroke="#3aaa35" stroke-width="2.5"><path d="M6 26 30 6l24 20M12 22v28h36V22M25 50V36h10v14"/></svg><span>Revovator</span></div>
<div class="abs cat" style="left:330px">
  <svg width="60" height="54" viewBox="0 0 60 54" fill="none" stroke="#3aaa35" stroke-width="2.5"><rect x="6" y="16" width="48" height="32" rx="3"/><path d="M22 16V9h16v7M6 28h48"/><circle cx="30" cy="32" r="6"/></svg><span>Tradie</span></div>
<div class="abs cat" style="left:517px">
  <svg width="60" height="54" viewBox="0 0 60 54" fill="none" stroke="#3aaa35" stroke-width="2.5"><path d="M8 50V24L30 8l22 16v26z"/><path d="M18 30h8v8h-8zM34 30h8v8h-8zM8 50h44"/></svg><span>Builder</span></div>
<div class="abs cat" style="left:702px">
  <svg width="60" height="54" viewBox="0 0 60 54" fill="none" stroke="#3aaa35" stroke-width="2.5"><rect x="6" y="16" width="48" height="32" rx="3"/><path d="M22 16V10h16v6M6 30h48"/></svg><span>Corporate</span></div>
<div class="abs cat" style="left:889px">
  <svg width="60" height="54" viewBox="0 0 60 54" fill="none" stroke="#3aaa35" stroke-width="2.5"><circle cx="30" cy="27" r="22"/><path d="M8 27h44M30 5c8 8 8 36 0 44M30 5c-8 8-8 36 0 44"/></svg><span>National</span></div>
<p class="abs tagline">Australia's Highest Rated Skip Bin Hire Company - Rated by You</p>

<!-- steps -->
<section class="abs steps"></section>
<h2 class="abs steps-title">As Easy As 1, 2, 3...</h2>
<div class="abs step-line"></div>
<div class="abs step-ring" style="top:1144px"><svg width="46" height="52" viewBox="0 0 46 52" fill="none" stroke="#fff" stroke-width="2"><path d="M4 2h28l10 10v38H4z"/><path d="M12 18h22M12 26h22M12 34h16"/></svg></div>
<div class="abs step-ring" style="top:1296px"><svg width="54" height="46" viewBox="0 0 54 46" fill="none" stroke="#fff" stroke-width="2"><rect x="3" y="12" width="48" height="32"/><path d="M3 12l24 18 24-18M10 18V3h34v15M16 10h22"/></svg></div>
<div class="abs step-ring" style="top:1440px"><svg width="58" height="58" viewBox="0 0 58 58" fill="none" stroke="#fff" stroke-width="2.5"><circle cx="29" cy="29" r="25"/><path d="M17 30l8 8 16-17"/></svg></div>
<div class="abs step-text" style="top:1172px"><h3>1. Simple, Easy Booking</h3><p>Call 1800 555 019 or click here to get started with your instant quote</p></div>
<div class="abs step-text" style="top:1320px"><h3>2. Instant Confirmation</h3><p>Receive your booking details and a 30 minute courtesy call before drop off</p></div>
<div class="abs step-text" style="top:1467px"><h3>3. Gone When Your Ready!</h3><p>Let us know and your bin will be gone within 24hrs</p></div>

<section class="abs video-panel"></section>
<div class="abs map-area" role="img" aria-label="Map of Australia with dotted delivery routes"></div>
<svg class="abs" style="left:836px;top:1229px" width="48" height="48" viewBox="0 0 48 48"><circle cx="24" cy="24" r="23" fill="#fff"/><path d="M19 14l14 10-14 10z" fill="#1f6b2a"/></svg>
<p class="abs video-text">We manage your booking from start to finish, so you can focus on other things</p>

<!-- testimonials -->
<h2 class="abs section-title" style="top:1712px;font-size:38px">Five Star Service</h2>
<svg class="abs" style="left:48px;top:1940px" width="14" height="24" viewBox="0 0 14 24"><path d="M12 2 3 12l9 10" stroke="#aaa" stroke-width="3" fill="none"/></svg>
<svg class="abs" style="left:1136px;top:1940px" width="14" height="24" viewBox="0 0 14 24"><path d="M2 2l9 10-9 10" stroke="#aaa" stroke-width="3" fill="none"/></svg>

<div class="abs review" style="left:160px;top:1834px;width:226px">
  <div class="avatar" style="width:88px;height:88px;margin:0 auto 26px" role="img" aria-label="Reviewer portrait"></div>
  <p style="font-size:12px">Easy to book through the website and great to have live chat facility. Bin was delivered as organised and all went well. Would use again.</p>
  <div class="who">Harriet</div><div class="date">10/04/2018</div>
  <div class="mini-stars"><i></i><i></i><i></i><i></i><i></i></div>
</div>

<div class="abs review-card"></div>
<div class="abs review" style="left:458px;top:1814px;width:284px">
  <div class="avatar" style="width:106px;height:106px;margin:0 auto 28px" role="img" aria-label="Reviewer portrait"></div>
  <p style="font-size:14.5px">Easy to organise delivered on time. Had the skip we required for a reasonable price would reccomend to anyone looking to hire a skip.</p>
  <div class="who" style="font-size:13px">Priya Calloway</div><div class="date" style="font-size:13px">02/06/2018</div>
  <div class="mini-stars review-card-stars"><i></i><i></i><i></i><i></i><i></i></div>
</div>

<div class="abs review" style="left:812px;top:1834px;width:230px">
  <div class="avatar" style="width:88px;height:88px;margin:0 auto 26px" role="img" aria-label="Reviewer portrait"></div>
  <p style="font-size:12px">The service from Tumble Crate Rentals Oz was great. The confirmation and correspondence by phone and email was very professional</p>
  <div class="who">Tobias Renwick</div><div class="date">10/04/2018</div>
  <div class="mini-stars"><i></i><i></i><i></i><i></i><i></i></div>
</div>

<!-- benefits -->
<section class="abs benefits"></section>
<h2 class="abs section-title" style="top:2288px;font-size:38px">Save Time. Save Money.</h2>
<div class="abs benefit" style="left:132px">
  <svg width="50" height="56" viewBox="0 0 50 56" fill="none" stroke="#3aaa35" stroke-width="2.5"><path d="M25 50S9 32 9 20a16 16 0 0 1 32 0c0 12-16 30-16 30z"/><circle cx="25" cy="20" r="6"/><path d="M4 54h42"/></svg>
  <h4>Any Bin, Anytime,<br>Anywhere</h4>
  <p>We connect you with local companies Australia wide, for faster response times, less km's and emissions, greater reliability and lower prices</p>
</div>
<div class="abs benefit" style="left:367px">
  <svg width="56" height="56" viewBox="0 0 56 56" fill="none" stroke="#3aaa35" stroke-width="2.5"><path d="M28 4 8 12v14c0 14 9 22 20 26 11-4 20-12 20-26V12z"/><path d="M18 28l7 7 13-14"/></svg>
  <h4>Service Guaranteed</h4>
  <p>Want to speak to someone when it suits you? We answer the phones and return calls from 7.30am to 8pm 7 days a week</p>
</div>
<div class="abs benefit" style="left:603px">
  <svg width="60" height="56" viewBox="0 0 60 56" fill="none" stroke="#3aaa35" stroke-width="2.5"><rect x="4" y="14" width="44" height="26" rx="2"/><circle cx="26" cy="27" r="7"/><path d="M10 46h44V20"/></svg>
  <h4>Best Pricing</h4>
  <p>We've done the hard work behind the scenes, so with one click you have your best priced, local skip</p>
</div>
<div class="abs benefit" style="left:838px">
  <svg width="64" height="56" viewBox="0 0 64 56" fill="none" stroke="#3aaa35" stroke-width="2.5"><path d="M4 22l12-12 16 8 16-8 12 12-16 18-12-8-12 8z"/><path d="M24 32l8 8M30 28l8 8"/></svg>
  <h4>First Class Supply<br>Partners</h4>
  <p>Our local supply partners are the best in the business and share our passion for making you happy</p>
</div>

<!-- cta -->
<section class="cta">
  <h2 class="abs cta-title">1000's of Skips at Your Finger Tips</h2>
  <p class="abs hero-sub cta-sub" style="top:2765px">BEST SERVICE &amp; PRICE &nbsp;•&nbsp; HASSLE FREE &nbsp;•&nbsp; AUSTRALIA WIDE</p>
  <div class="abs quote-box" style="top:2807px"><span>Enter Postcode or Suburb</span><div class="quote-btn">INSTANT QUOTE</div></div>
  <div class="abs stars" style="top:2875px">
    <svg width="130" height="26" viewBox="0 0 130 26"><g fill="#f5c518"><use href="#s"/><use href="#s" x="26"/><use href="#s" x="52"/><use href="#s" x="78"/><use href="#s" x="104"/></g></svg>
  </div>
</section>

<!-- footer -->
<footer class="abs site-footer"></footer>
<div class="abs fcol" style="left:145px;top:3020px"><h5 class="fcol-wide">Tumble Crate Rentals Oz - Australia Wide</h5><ul><li>Sydney</li><li>Melbourne</li><li>Brisbane</li><li>Perth</li><li>Adelaide</li><li>Canberra</li></ul></div>
<div class="abs fcol" style="left:482px;top:3020px"><h5>Learn More</h5><ul><li>Waste Types</li><li>Skip Bin Sizes</li><li>Refund Policy</li><li>Pay Later with FlexPay</li><li>FAQ</li><li>Privacy</li></ul></div>
<div class="abs fcol" style="left:660px;top:3020px"><h5>Links</h5><ul><li>Pricing</li><li>About</li><li>Trade Secrets</li><li>Contact</li><li>Login</li><li>Create Account</li></ul></div>
<div class="abs fcol" style="left:837px;top:3020px"><h5>Newsletter</h5></div>
<div class="abs news-input">Email Address
  <svg width="18" height="14" viewBox="0 0 18 14"><rect width="18" height="14" fill="#24235c"/><path d="M1 1l8 6 8-6" stroke="#cfd0e6" stroke-width="1.5" fill="none"/></svg></div>
<p class="abs copyright">Copyright © 2019 TUMBLE CRATE RENTALS OZ. All rights reserved.</p>
<div class="abs pay" style="left:702px;width:24px"></div>
<div class="abs pay" style="left:742px;width:36px"></div>
<div class="abs pay" style="left:792px;width:30px"></div>
<div class="abs pay" style="left:836px;width:34px"></div>
<div class="abs pay" style="left:882px;width:62px"></div>
<div class="abs social" style="left:964px"></div>
<div class="abs social" style="left:998px"></div>
<div class="abs social" style="left:1040px"></div>

</body>
</html>
```